Need Letterhead Design & Matching Business Card

I have a logo that I love already. But the letterhead is less than appealing and boring. I'd like a design for my letterhead which I will match with business cards. Also, I'd like to have used fonts that are generally available, as my current letterhead uses a font named "SPACE" which nobody has unless they download it...so when a Word version is forwarded, it looks awful on the receiver's screed due to not having the font. That being said, modern is the look we like and are going for.

My business is "Halloran Brightmoor PC" - a law firm specializing in representing people who have suffered catastrophic injuries or death (plane, auto, train crashes etc.).

See attached letterhead, which has all of the pertinent information. My logo is also attached in various formats.

```html
<!DOCTYPE html>
<html lang="en">
<head>
<meta charset="utf-8">
<title>Halloran Brightmoor PC — Letterhead &amp; Business Card</title>
<link href="https://fonts.googleapis.com/css2?family=Montserrat:wght@300;400;600&family=Open+Sans:wght@400;600&display=swap" rel="stylesheet">
<style>
  :root{
    --ink:#1d1d1f;
    --charcoal:#2b2b2d;
    --charcoal-soft:#3a3a3d;
    --gold:#c8a765;
    --gold-light:#e2cd98;
    --paper:#ffffff;
    --panel:#e9e9ea;
    --text:#4a4a4c;
    --muted:#8d8d90;
    --wordmark:#d9d9db;
  }
  *{box-sizing:border-box;margin:0;padding:0}
  html,body{width:691px;height:1200px;overflow:hidden;background:var(--charcoal)}
  body{font-family:"Open Sans",Arial,sans-serif;color:var(--text);position:relative}

  .showcase-top{position:absolute;left:0;top:0;width:691px;height:540px;background:var(--charcoal)}
  .showcase-bottom{position:absolute;left:0;top:540px;width:691px;height:600px;background:var(--paper)}
  .showcase-footer{position:absolute;left:0;top:1140px;width:691px;height:60px;background:var(--ink)}

  /* Wordmark */
  .wordmark{display:flex;align-items:center;gap:14px;font-family:"Montserrat",Arial,sans-serif;font-weight:300;letter-spacing:.32em;text-transform:uppercase;white-space:nowrap}
  .wordmark__square{width:16px;height:16px;background:var(--gold);flex:none}
  .wordmark--hero{position:absolute;left:0;right:0;top:458px;justify-content:center;color:var(--wordmark);font-size:19px}
  .wordmark--hero .wordmark__square{width:26px;height:26px}

  /* Letterhead */
  .letterhead{position:absolute;width:335px;height:570px;background:var(--paper);overflow:hidden;box-shadow:0 2px 10px rgba(0,0,0,.18)}
  .letterhead--presentation{left:235px;top:28px;transform:scale(.66);transform-origin:top left}
  .letterhead--detail{left:346px;top:556px}
  .letterhead__header{position:absolute;left:0;top:0;width:100%;height:58px}
  .letterhead__header svg{position:absolute;inset:0}
  .letterhead__brand{position:absolute;left:20px;top:16px;color:#fff;font-size:8.5px;gap:7px;letter-spacing:.24em;line-height:1.35;align-items:flex-start}
  .letterhead__brand .wordmark__square{width:14px;height:14px;margin-top:2px}
  .letterhead__tagline{position:absolute;right:18px;top:26px;font-family:"Montserrat",Arial,sans-serif;font-size:4.6px;letter-spacing:.2em;color:var(--gold);text-transform:uppercase}
  .letterhead__body{position:absolute;left:26px;top:84px;width:270px;font-size:5px;line-height:1.65}
  .letterhead__date{margin-bottom:12px}
  .letterhead__recipient{margin-bottom:12px}
  .letterhead__recipient strong{display:block;font-family:"Montserrat",Arial,sans-serif;font-weight:600;color:var(--ink);font-size:6px;letter-spacing:.06em}
  .letterhead__body p{margin-bottom:8px;text-align:justify}
  .letterhead__signoff{margin-top:10px}
  .letterhead__signature{display:block;width:70px;height:16px;margin:6px 0 2px}
  .letterhead__signer{font-family:"Montserrat",Arial,sans-serif;font-weight:600;color:var(--ink);font-size:5.4px;letter-spacing:.06em;text-decoration:underline}
  .letterhead__contact{position:absolute;right:26px;bottom:44px;text-align:right;font-size:4.4px;line-height:1.7;color:var(--muted)}
  .letterhead__tab{position:absolute;right:0;top:440px;width:12px;height:80px;background:var(--charcoal);display:flex;flex-direction:column;align-items:center;justify-content:space-evenly}
  .letterhead__tab svg{width:6px;height:6px}
  .letterhead__foot{position:absolute;left:0;bottom:0;width:100%;height:16px;background:var(--charcoal)}
  .letterhead__foot::before{content:"";position:absolute;left:0;top:0;width:90px;height:2px;background:var(--gold)}

  /* Business card */
  .card-stage{position:absolute;left:0;top:0;width:330px;height:300px;background:var(--panel)}
  .business-card{position:absolute;left:115px;top:55px;width:108px;height:190px;background:var(--ink);border-radius:3px;box-shadow:0 6px 16px rgba(0,0,0,.25);display:flex;flex-direction:column;align-items:center;justify-content:center;gap:10px}
  .business-card .wordmark__square{width:20px;height:20px}
  .business-card__name{font-family:"Montserrat",Arial,sans-serif;font-weight:300;letter-spacing:.22em;color:#fff;font-size:6.5px;text-align:center;line-height:1.6;text-transform:uppercase}

  .gold-pattern{position:absolute;left:0;top:300px;width:330px;height:300px;background:linear-gradient(135deg,var(--gold) 0%,var(--gold-light) 55%,var(--gold) 100%)}
</style>
</head>
<body>

<section class="showcase-top">
  <article class="letterhead letterhead--presentation">
    <header class="letterhead__header">
      <svg viewBox="0 0 335 58" preserveAspectRatio="none" aria-hidden="true">
        <polygon points="0,0 335,0 335,40 210,40 196,58 0,58" fill="#1d1d1f"/>
      </svg>
      <div class="wordmark letterhead__brand"><span class="wordmark__square"></span><span>Halloran<br>Brightmoor PC</span></div>
      <div class="letterhead__tagline">Injury &amp; Wrongful Death</div>
    </header>
    <div class="letterhead__body">
      <div class="letterhead__date">15 March 2024</div>
      <div class="letterhead__recipient"><strong>DANIEL FORSYTHE</strong>Product Manager<br>4180 Larkspur Blvd | Suite 310<br>Fairhaven, CA 90417</div>
      <p>Dear Mr. Forsythe,</p>
      <p>Lorem ipsum dolor sit amet, consectetur adipiscing elit, sed do eiusmod tempor incididunt ut labore et dolore magna aliqua. Ut enim ad minim veniam, quis nostrud exercitation ullamco laboris nisi ut aliquip ex ea commodo consequat. Duis aute irure dolor in reprehenderit in voluptate velit esse cillum dolore eu fugiat nulla pariatur.</p>
      <p>Excepteur sint occaecat cupidatat non proident, sunt in culpa qui officia deserunt mollit anim id est laborum. Sed ut perspiciatis unde omnis iste natus error sit voluptatem accusantium doloremque laudantium, totam rem aperiam eaque ipsa quae ab illo inventore veritatis.</p>
      <p>Nemo enim ipsam voluptatem quia voluptas sit aspernatur aut odit aut fugit, sed quia consequuntur magni dolores eos qui ratione voluptatem sequi nesciunt. Neque porro quisquam est qui dolorem ipsum quia dolor sit amet, consectetur, adipisci velit, sed quia non numquam eius modi tempora incidunt.</p>
      <p>At vero eos et accusamus et iusto odio dignissimos ducimus qui blanditiis praesentium voluptatum deleniti atque corrupti quos dolores.</p>
      <div class="letterhead__signoff">Sincerely,
        <svg class="letterhead__signature" viewBox="0 0 70 16" aria-hidden="true"><path d="M2 12 C10 2 14 2 12 10 S22 4 28 9 S40 3 46 10 S60 6 68 8" fill="none" stroke="#1d1d1f" stroke-width="1"/></svg>
        <span class="letterhead__signer">R. COLE PENDER, ESQ.</span><br>Principal
      </div>
    </div>
    <div class="letterhead__contact">tel 415 555 0182<br>fax 415 555 0183<br>office@hallorantest.law<br>2200 Mercer Plaza, Suite 900<br>Fairhaven, CA 90417</div>
    <div class="letterhead__tab">
      <svg viewBox="0 0 6 6" aria-hidden="true"><path d="M1 .5 L2.2 .5 L2.6 2 L1.9 2.5 Q2.6 3.7 3.5 4.1 L4 3.4 L5.5 3.8 L5.5 5 Q2 5.3 .7 1.5 Z" fill="#c8a765"/></svg>
      <svg viewBox="0 0 6 6" aria-hidden="true"><path d="M3 .4 A1.9 1.9 0 0 1 4.9 2.3 C4.9 3.6 3 5.6 3 5.6 S1.1 3.6 1.1 2.3 A1.9 1.9 0 0 1 3 .4 Z" fill="#c8a765"/></svg>
      <svg viewBox="0 0 6 6" aria-hidden="true"><rect x=".5" y="1.3" width="5" height="3.4" fill="none" stroke="#c8a765" stroke-width=".6"/><path d="M.5 1.3 L3 3.3 L5.5 1.3" fill="none" stroke="#c8a765" stroke-width=".6"/></svg>
    </div>
    <div class="letterhead__foot"></div>
  </article>

  <div class="wordmark wordmark--hero"><span>Halloran</span><span class="wordmark__square"></span><span>Brightmoor PC</span></div>
</section>

<section class="showcase-bottom">
  <div class="card-stage">
    <div class="business-card">
      <span class="wordmark__square"></span>
      <div class="business-card__name">Halloran<br>Brightmoor PC</div>
    </div>
  </div>
  <div class="gold-pattern" role="img" aria-label="Gold geometric brand pattern"></div>
</section>

<article class="letterhead letterhead--detail">
  <header class="letterhead__header">
    <svg viewBox="0 0 335 58" preserveAspectRatio="none" aria-hidden="true">
      <polygon points="0,0 335,0 335,40 210,40 196,58 0,58" fill="#1d1d1f"/>
    </svg>
    <div class="wordmark letterhead__brand"><span class="wordmark__square"></span><span>Halloran<br>Brightmoor PC</span></div>
    <div class="letterhead__tagline">Injury &amp; Wrongful Death</div>
  </header>
  <div class="letterhead__body">
    <div class="letterhead__date">15 March 2024</div>
    <div class="letterhead__recipient"><strong>DANIEL FORSYTHE</strong>Product Manager<br>4180 Larkspur Blvd | Suite 310<br>Fairhaven, CA 90417</div>
    <p>Dear Mr. Forsythe,</p>
    <p>Lorem ipsum dolor sit amet, consectetur adipiscing elit, sed do eiusmod tempor incididunt ut labore et dolore magna aliqua. Ut enim ad minim veniam, quis nostrud exercitation ullamco laboris nisi ut aliquip ex ea commodo consequat. Duis aute irure dolor in reprehenderit in voluptate velit esse cillum dolore eu fugiat nulla pariatur.</p>
    <p>Excepteur sint occaecat cupidatat non proident, sunt in culpa qui officia deserunt mollit anim id est laborum. Sed ut perspiciatis unde omnis iste natus error sit voluptatem accusantium doloremque laudantium, totam rem aperiam eaque ipsa quae ab illo inventore veritatis.</p>
    <p>Nemo enim ipsam voluptatem quia voluptas sit aspernatur aut odit aut fugit, sed quia consequuntur magni dolores eos qui ratione voluptatem sequi nesciunt. Neque porro quisquam est qui dolorem ipsum quia dolor sit amet, consectetur, adipisci velit, sed quia non numquam eius modi tempora incidunt.</p>
    <p>At vero eos et accusamus et iusto odio dignissimos ducimus qui blanditiis praesentium voluptatum deleniti atque corrupti quos dolores.</p>
    <div class="letterhead__signoff">Sincerely,
      <svg class="letterhead__signature" viewBox="0 0 70 16" aria-hidden="true"><path d="M2 12 C10 2 14 2 12 10 S22 4 28 9 S40 3 46 10 S60 6 68 8" fill="none" stroke="#1d1d1f" stroke-width="1"/></svg>
      <span class="letterhead__signer">R. COLE PENDER, ESQ.</span><br>Principal
    </div>
  </div>
  <div class="letterhead__contact">tel 415 555 0182<br>fax 415 555 0183<br>office@hallorantest.law<br>2200 Mercer Plaza, Suite 900<br>Fairhaven, CA 90417</div>
  <div class="letterhead__tab">
    <svg viewBox="0 0 6 6" aria-hidden="true"><path d="M1 .5 L2.2 .5 L2.6 2 L1.9 2.5 Q2.6 3.7 3.5 4.1 L4 3.4 L5.5 3.8 L5.5 5 Q2 5.3 .7 1.5 Z" fill="#c8a765"/></svg>
    <svg viewBox="0 0 6 6" aria-hidden="true"><path d="M3 .4 A1.9 1.9 0 0 1 4.9 2.3 C4.9 3.6 3 5.6 3 5.6 S1.1 3.6 1.1 2.3 A1.9 1.9 0 0 1 3 .4 Z" fill="#c8a765"/></svg>
    <svg viewBox="0 0 6 6" aria-hidden="true"><rect x=".5" y="1.3" width="5" height="3.4" fill="none" stroke="#c8a765" stroke-width=".6"/><path d="M.5 1.3 L3 3.3 L5.5 1.3" fill="none" stroke="#c8a765" stroke-width=".6"/></svg>
  </div>
  <div class="letterhead__foot"></div>
</article>

<footer class="showcase-footer"></footer>

</body>
</html>
```